Post Card (5x7) - Pre-foreclosure Image - Harbor Path Partners

(Two-Sided Post Card)
FACING FORECLOSURE? YOU STILL HAVE OPTIONS.
If you’re behind on payments or at risk of foreclosure, you’re not alone—and it’s not too late to take action.
We help homeowners:
• Explore options to stay in their home
• Stop or delay foreclosure
• Sell quickly for a fair price if needed
No pressure. No obligation. Just real solutions tailored to your situation.
Call - (240) 558-2094
Email - marcus@hpbllc-mail.com
Harbor Path Partners LLC
7200 Bramwick Lane, Ellicott City, MD 21043
**Marcus Fennimore is a Licensed Realtor with Copperleaf Homes Realty in Bethesda, Maryland.
(Leave room for mailing address, return address & postage)
Target Market(s)
Distressed Homeowners
Industry/Entity Type
Real Estate

```html
<!DOCTYPE html>
<html lang="en">
<head>
<meta charset="utf-8">
<title>Harbor Path Partners – Pre-foreclosure Postcard</title>
<link href="https://fonts.googleapis.com/css2?family=Bebas+Neue&family=Montserrat:ital,wght@0,300;0,400;0,500;0,600;0,700;1,400;1,600;1,700&display=swap" rel="stylesheet">
<style>
  :root{
    --canvas:#e8e8ea;
    --yellow:#f6d316;
    --ink:#151515;
    --white:#ffffff;
    --band:#0d0d0d;
    --sky-top:#4d4a48;
    --sunset:#b07a4a;
    --city:#262322;
    --water:#3a3431;
  }
  *{box-sizing:border-box;margin:0;padding:0}
  html,body{width:1200px;height:1200px;overflow:hidden}
  body{background:var(--canvas);position:relative;font-family:"Montserrat",sans-serif}

  .card{position:absolute;left:247px;width:706px;height:504px;overflow:hidden}
  .card--front{top:80px}
  .card--back{top:616px;background:var(--white)}

  /* FRONT */
  .front-photo{position:absolute;inset:0;
    background:
      radial-gradient(ellipse 30% 22% at 88% 52%, rgba(214,132,62,.75), transparent 70%),
      radial-gradient(ellipse 25% 18% at 6% 48%, rgba(190,120,70,.55), transparent 70%),
      linear-gradient(180deg,var(--sky-top) 0%,#6a5f57 30%,var(--sunset) 50%,var(--city) 62%,var(--city) 72%,var(--water) 100%);}
  .front-frame{position:absolute;inset:0;width:100%;height:100%}
  .front-content{position:absolute;inset:0;text-align:center;color:var(--white)}
  .headline{position:absolute;top:28px;left:0;right:0;font-family:"Bebas Neue",sans-serif;font-size:66px;line-height:1;letter-spacing:-.5px}
  .headline .accent{color:var(--yellow)}
  .options-pill{position:absolute;left:192px;top:98px;width:323px;height:32px;border-radius:16px;background:var(--yellow);
    font-weight:700;font-size:20px;line-height:32px;color:var(--white);letter-spacing:.3px}
  .intro{position:absolute;top:137px;left:0;right:0;font-size:11.6px;font-weight:300;line-height:15px}
  .brand-front{position:absolute;top:188px;left:0;right:0;display:flex;flex-direction:column;align-items:center;gap:12px}
  .brand-mark{width:26px;height:26px;border:2px solid var(--white)}
  .brand-name{font-size:19px;font-weight:500;letter-spacing:3px;line-height:1.2}
  .help-title{position:absolute;top:281px;left:0;right:0;font-size:14px;font-weight:400;letter-spacing:.4px}
  .service{position:absolute;top:313px;width:136px;margin-left:-68px;display:flex;flex-direction:column;align-items:center}
  .service svg{width:44px;height:44px}
  .service p{margin-top:8px;font-size:14px;font-weight:600;line-height:18px}
  .front-phone{position:absolute;top:445px;left:0;right:0;font-family:"Bebas Neue",sans-serif;font-size:27px;letter-spacing:.3px}

  /* BACK */
  .back-hero{position:absolute;left:0;top:0;width:706px;height:277px;
    background:linear-gradient(90deg,#b9aaa9 0%,#d8cbcc 25%,#efe7ea 45%,#faf7f8 60%,#ffffff 75%)}
  .portrait{position:absolute;left:0;top:24px;width:209px;height:253px;
    background:linear-gradient(180deg,#3a3a3c 0%,#1e1e20 45%,#121214 100%);border-radius:90px 90px 0 0}
  .brand-back{position:absolute;top:38px;left:226px;width:200px;display:flex;flex-direction:column;align-items:center;gap:10px;color:var(--ink)}
  .brand-back .brand-mark{border-color:var(--ink)}
  .brand-back .brand-name{text-align:center}
  .contact{position:absolute;left:226px;width:200px;display:flex;justify-content:center;align-items:center;gap:6px;color:var(--ink)}
  .contact svg{width:16px;height:16px;flex:none}
  .contact--phone{top:129px;font-size:17px;font-weight:500}
  .contact--email{top:156px;font-size:15.5px;font-weight:500;left:200px;width:260px}
  .contact--address{top:180px;align-items:flex-start;font-size:11.5px;font-weight:600;line-height:16px}
  .contact--address svg{width:12px;height:12px;margin-top:2px}
  .agent-band{position:absolute;left:209px;top:227px;width:497px;height:50px;background:var(--band);color:var(--white);
    padding:7px 0 0 23px;font-style:italic;font-size:12px;line-height:17px}
  .agent-band strong{font-size:15px;font-weight:700}
  .promise{position:absolute;left:53px;width:242px;background:var(--yellow);border-radius:0 18px 18px 0;
    padding-left:25px;display:flex;align-items:center;font-style:italic;font-weight:600;font-size:15px;color:var(--ink);line-height:19px}
  .promise--1{top:308px;height:30px}
  .promise--2{top:353px;height:30px}
  .promise--3{top:398px;height:50px;border-radius:0 25px 25px 0}
  .tick{position:absolute;left:-14px;width:28px;height:28px}
</style>
</head>
<body>

<section class="card card--front">
  <div class="front-photo" role="img" aria-label="City skyline silhouetted at sunset above a river"></div>
  <svg class="front-frame" viewBox="0 0 1136 811" preserveAspectRatio="none" aria-hidden="true">
    <polygon points="145,-10 992,-10 992,618 640,811 495,811 145,618" fill="rgba(20,18,18,.42)" stroke="rgba(255,255,255,.62)" stroke-width="16"/>
    <polyline points="385,455 205,560 205,811" fill="none" stroke="rgba(255,255,255,.55)" stroke-width="2"/>
    <polyline points="760,455 935,560 935,811" fill="none" stroke="rgba(255,255,255,.55)" stroke-width="2"/>
  </svg>
  <div class="front-content">
    <h1 class="headline">Facing <span class="accent">Foreclosure?</span></h1>
    <div class="options-pill">YOU STILL HAVE OPTIONS.</div>
    <p class="intro">If you’re behind on payments or at risk of foreclosure,<br>you’re not alone—and it’s not too late to take action.</p>
    <div class="brand-front">
      <span class="brand-mark"></span>
      <span class="brand-name">HARBOR PATH PARTNERS LLC</span>
    </div>
    <p class="help-title">WE HELP HOMEOWNERS</p>

    <div class="service" style="left:218px">
      <svg viewBox="0 0 44 44" aria-hidden="true"><circle cx="22" cy="22" r="20.5" fill="none" stroke="var(--yellow)" stroke-width="1.6"/><circle cx="20" cy="20" r="7" fill="none" stroke="var(--yellow)" stroke-width="1.6"/><line x1="25" y1="25" x2="31" y2="31" stroke="var(--yellow)" stroke-width="2.2" stroke-linecap="round"/></svg>
      <p>Explore options to stay in their home</p>
    </div>
    <div class="service" style="left:352px">
      <svg viewBox="0 0 44 44" aria-hidden="true"><circle cx="22" cy="22" r="20.5" fill="none" stroke="var(--yellow)" stroke-width="1.6"/><rect x="15" y="12" width="12" height="6" rx="1" fill="none" stroke="var(--yellow)" stroke-width="1.6"/><line x1="21" y1="18" x2="21" y2="26" stroke="var(--yellow)" stroke-width="1.6"/><rect x="12" y="26" width="20" height="6" rx="1" fill="none" stroke="var(--yellow)" stroke-width="1.6"/></svg>
      <p>Stop or delay foreclosure</p>
    </div>
    <div class="service" style="left:488px">
      <svg viewBox="0 0 44 44" aria-hidden="true"><circle cx="22" cy="22" r="20.5" fill="none" stroke="var(--yellow)" stroke-width="1.6"/><path d="M13 19h5l9-5v16l-9-5h-5z" fill="none" stroke="var(--yellow)" stroke-width="1.6" stroke-linejoin="round"/><line x1="16" y1="25" x2="18" y2="31" stroke="var(--yellow)" stroke-width="1.6"/></svg>
      <p>Sell quickly for a fair price if needed</p>
    </div>

    <p class="front-phone">(240) 558-2094</p>
  </div>
</section>

<section class="card card--back">
  <div class="back-hero" role="img" aria-label="Faded city buildings fading into white"></div>
  <div class="portrait" role="img" aria-label="Portrait of the realtor in a dark hat and jacket"></div>

  <div class="brand-back">
    <span class="brand-mark"></span>
    <span class="brand-name">HARBOR PATH PARTNERS LLC</span>
  </div>

  <p class="contact contact--phone">
    <svg viewBox="0 0 16 16" aria-hidden="true"><circle cx="8" cy="8" r="8" fill="var(--ink)"/><path d="M5.5 4.5l1.4 1.6-.8 1c.5 1 1.3 1.8 2.3 2.3l1-.8 1.6 1.4-.9 1.3c-2.6-.4-4.9-2.7-5.3-5.3z" fill="var(--white)"/></svg>
    (240) 558-2094
  </p>
  <p class="contact contact--email">
    <svg viewBox="0 0 16 16" aria-hidden="true"><circle cx="8" cy="8" r="8" fill="var(--ink)"/><rect x="4" y="5.2" width="8" height="5.6" fill="none" stroke="var(--white)" stroke-width="1"/><path d="M4 5.4l4 3 4-3" fill="none" stroke="var(--white)" stroke-width="1"/></svg>
    marcus@hpbllc-mail.com
  </p>
  <p class="contact contact--address">
    <svg viewBox="0 0 12 12" aria-hidden="true"><path d="M6 .5a4 4 0 0 1 4 4c0 3-4 7-4 7s-4-4-4-7a4 4 0 0 1 4-4z" fill="var(--ink)"/><circle cx="6" cy="4.5" r="1.5" fill="var(--white)"/></svg>
    <span>7200 Bramwick Lane,<br>Ellicott City, MD 21043</span>
  </p>

  <div class="agent-band">
    <strong>Marcus Fennimore</strong> is a Licensed Realtor<br>with Copperleaf Homes Realty in Bethesda, Maryland.
  </div>

  <div class="promise promise--1">
    <svg class="tick" viewBox="0 0 28 28" aria-hidden="true"><circle cx="14" cy="14" r="13" fill="var(--yellow)" stroke="var(--white)" stroke-width="2.5"/><path d="M9 14.5l3.2 3.2L19 10" fill="none" stroke="var(--white)" stroke-width="2" stroke-linecap="round" stroke-linejoin="round"/></svg>
    No pressure.
  </div>
  <div class="promise promise--2">
    <svg class="tick" viewBox="0 0 28 28" aria-hidden="true"><circle cx="14" cy="14" r="13" fill="var(--yellow)" stroke="var(--white)" stroke-width="2.5"/><path d="M9 14.5l3.2 3.2L19 10" fill="none" stroke="var(--white)" stroke-width="2" stroke-linecap="round" stroke-linejoin="round"/></svg>
    No obligation.
  </div>
  <div class="promise promise--3">
    <svg class="tick" viewBox="0 0 28 28" aria-hidden="true"><circle cx="14" cy="14" r="13" fill="var(--yellow)" stroke="var(--white)" stroke-width="2.5"/><path d="M9 14.5l3.2 3.2L19 10" fill="none" stroke="var(--white)" stroke-width="2" stroke-linecap="round" stroke-linejoin="round"/></svg>
    Just real solutions<br>tailored to your situation.
  </div>
</section>

</body>
</html>
```